Flyer-Gestaltung für Pelz- & Gold-Ankauf
Zielgruppe
Pelz & Gold Ankauf Wendtner in Ottobrunn
Unsere Zielgruppe sind Rentner und Senioren
Wir kaufen Pelze Gold und Bernstein auf
Aber Hauptsächlich geht es um den Pelzankauf
Daher suchen wir ein hochwertiges Design was direkt ins Auge fällt
Aufgabenstellung
Wir brauchen ein vertrauenswürdiges und gleich auffälliges Inserat mit sehr hochwertigen Bildern und kleinen seriösen Texten.
Der größte Teil der Werbung sollte für die Pelze sein und ein kleiner für Bernstein und Goldschmuck.
Folgende Vorgaben müssen berücksichtigt werden:
- 231mm breite und 324mm Höhe
- Hochformat in der Zeitung
Für den Text sind folgende Informationen zu integrieren:
Wichtig wäre das unsere Pelz Aktion gilt nur 4 - 6 Tage
Wir zahlen bis zu 10 000 für Pelze
Unser Ankauf ist in ganz Ottobrunn, Unterhaching, Feldmoching, Aying Brunthal, Germering, Garching und Umgebung
Information zu den Anhängen:
Das 1 Bild war unsere alte Anzeige von damals aber die nicht grade besonders ist
Das 2 Bild und 3 Bild wäre die Konkurrenz
Es sollte selbstverständlich in jedem Punkt besser ausschauen
Wir möchten nicht der Konkurrenz ähneln
Bild 4 wäre ein Design wo uns gut gefällt von einen Bernstein Ankauf
Es sollte direkt ins Auge fallen
Ich hoffe auf ein auffälliges besonderes Design das die Leute überzeugt lieber bei mir ihren Pelz zu verkaufen

```html
<!DOCTYPE html>
<html lang="de">
<head>
<meta charset="utf-8">
<title>Wendtner Pelz &amp; Goldankauf – Flyer</title>
<link href="https://fonts.googleapis.com/css2?family=Jost:wght@400;500;600&family=Encode+Sans+Semi+Condensed:wght@400;600;700&display=swap" rel="stylesheet">
<style>
  :root {
    --page: #ffffff;
    --slate: #454851;
    --cream: #f7eeb0;
    --white: #ffffff;
    --rule: #a9a9ad;
    --fur-white: #f1efec;
    --fur-light: #e4e0da;
    --fur-grey: #9c9a9c;
    --fur-beige: #d6cfc6;
    --fur-dark: #1b1c21;
    --gold-light: #f4d98a;
    --gold: #d8b253;
  }
  * { margin: 0; padding: 0; box-sizing: border-box; }
  html, body { width: 1200px; height: 1200px; overflow: hidden; background: var(--page); }
  .flyer {
    position: absolute; left: 336px; top: 228px;
    width: 528px; height: 744px;
    background: var(--slate); overflow: hidden;
    font-family: "Encode Sans Semi Condensed", "Arial Narrow", sans-serif;
    color: var(--white);
  }
  .hero { position: absolute; left: 0; top: 0; width: 528px; height: 290px; }
  .brand-owner {
    position: absolute; top: 296px; width: 100%; text-align: center;
    font-family: "Jost", sans-serif; font-size: 18px; font-weight: 400; color: var(--white);
  }
  .brand-title {
    position: absolute; top: 314px; width: 100%; text-align: center;
    font-family: "Jost", sans-serif; font-size: 40px; font-weight: 600; color: var(--cream);
    letter-spacing: 0.2px;
  }
  .goods {
    position: absolute; left: 0; width: 100%; text-align: center;
    font-family: "Jost", sans-serif; font-size: 17px; font-weight: 400; color: var(--cream);
    word-spacing: 8px;
  }
  .goods.row1 { top: 368px; }
  .goods.row2 { top: 393px; }
  .goods.row3 { top: 418px; left: 4px; }
  .gold-visual { position: absolute; left: 30px; top: 464px; width: 160px; height: 160px; }
  .copy {
    position: absolute; left: 222px; top: 445px; width: 300px;
    font-size: 11.8px; line-height: 13px; color: var(--white);
  }
  .copy p { margin-bottom: 13px; }
  .copy .initial { font-size: 20px; line-height: 13px; }
  .copy .callout { color: var(--cream); font-weight: 700; display: block; }
  .copy .phone { color: var(--cream); }
  .copy .note { font-size: 10.5px; line-height: 13px; }
  .divider { position: absolute; left: 18px; top: 672px; width: 483px; height: 2px; background: var(--rule); }
  .offer {
    position: absolute; top: 678px; left: 0; width: 100%; text-align: center;
    font-size: 14.5px; line-height: 20.5px; font-weight: 700; color: var(--white);
  }
  .offer span { display: block; }
  .badge {
    position: absolute; top: 700px;
    font-size: 25px; font-weight: 700; color: var(--cream);
  }
  .badge.left { left: 24px; }
  .badge.right { right: 23px; }
</style>
</head>
<body>
  <main class="flyer">
    <svg class="hero" viewBox="0 0 528 290" role="img" aria-label="Foto: helle Pelzmäntel in Weiß, Grau und Creme auf einer Kleiderstange vor dunklem Hintergrund">
      <defs>
        <linearGradient id="furTone" x1="0" y1="0" x2="1" y2="0">
          <stop offset="0" stop-color="var(--fur-light)"/>
          <stop offset="0.12" stop-color="var(--fur-white)"/>
          <stop offset="0.2" stop-color="#b9b6b3"/>
          <stop offset="0.3" stop-color="var(--fur-white)"/>
          <stop offset="0.4" stop-color="var(--fur-light)"/>
          <stop offset="0.5" stop-color="var(--fur-grey)"/>
          <stop offset="0.6" stop-color="#c8c4bf"/>
          <stop offset="0.7" stop-color="var(--fur-beige)"/>
          <stop offset="0.82" stop-color="#e2ddd5"/>
          <stop offset="1" stop-color="#c3bcb4"/>
        </linearGradient>
        <linearGradient id="topShade" x1="0.1" y1="0.55" x2="0.35" y2="0">
          <stop offset="0" stop-color="var(--fur-dark)" stop-opacity="0"/>
          <stop offset="0.55" stop-color="var(--fur-dark)" stop-opacity="0.35"/>
          <stop offset="1" stop-color="var(--fur-dark)" stop-opacity="0.95"/>
        </linearGradient>
      </defs>
      <rect width="528" height="290" fill="url(#furTone)"/>
      <rect width="528" height="290" fill="url(#topShade)"/>
      <path d="M0 232 Q264 340 528 232 L528 290 L0 290 Z" fill="var(--slate)"/>
      <path d="M0 232 Q264 340 528 232" fill="none" stroke="var(--cream)" stroke-width="3"/>
    </svg>

    <div class="brand-owner">Wendtner</div>
    <h1 class="brand-title">Pelz &amp; Goldankauf</h1>

    <div class="goods row1">RINGE BROSCHEN</div>
    <div class="goods row2">MÜNZEN ALTGOLD BERNSTEIN</div>
    <div class="goods row3">U.V.M</div>

    <svg class="gold-visual" viewBox="0 0 160 160" role="img" aria-label="Illustration: Goldbarren, Sanduhr und Goldmünzen">
      <defs>
        <radialGradient id="goldTone" cx="0.5" cy="0.5" r="0.5">
          <stop offset="0" stop-color="var(--gold-light)"/>
          <stop offset="0.55" stop-color="var(--gold)" stop-opacity="0.85"/>
          <stop offset="1" stop-color="var(--gold)" stop-opacity="0"/>
        </radialGradient>
      </defs>
      <rect width="160" height="160" fill="url(#goldTone)"/>
    </svg>

    <div class="copy">
      <p><span class="initial">G</span>old &amp; Pelzankauf war noch nie so einfach!<br>
      Wendtner zahlt Ihnen Höchstpreise.<br>
      Profitieren Sie jetzt von unserem Angebot.<br>
      Jahrzehntelanger, verstaubter Schmuck ist<br>
      bares Geld wert.</p>
      <p>Unser Ankauf ist in ganz Ottobrunn, Unterhaching,<br>
      Feldmoching, Aying Brunthal, Germering, Garching<br>
      und Umgebung</p>
      <p><span class="callout">NUTZEN SIE DIESE EINMALIGE GELEGENHEIT!</span>
      Bei Fragen stehen wir Ihnen sehr gerne unter<br>
      der Tel.Nr.<span class="phone">+49 89 4412 7730</span> zur Verfügung.*</p>
      <p class="note">* Unsere Bürozeiten entnehmen Sie bitte unserer Website:<br>
      www.wendtner-ankauf.de</p>
    </div>

    <div class="divider"></div>

    <div class="badge left">AKTION!</div>
    <div class="offer">
      <span>WIR ZAHLEN BIS ZU 10.000 EURO FÜR IHREN PELZ!</span>
      <span>ABER NUR 4 TAGE LANG!</span>
      <span>GÜLTIG VOM 02 - 06 AUGUST 2021</span>
    </div>
    <div class="badge right">AKTION!</div>
  </main>
</body>
</html>
```